Thornvale Goods Co Box Label

I am putting together a kit made up of beard products (oils,balms etc) which i am calling a "Rugged Ritual Chest". I need to make a label for the box which includes my logo (attached) and would like a bearded man on it as well

```html
<!DOCTYPE html>
<html lang="en">
<head>
<meta charset="utf-8">
<title>Thornvale Goods Co – Rugged Ritual Chest Label</title>
<link href="https://fonts.googleapis.com/css2?family=Bebas+Neue&family=Oswald:wght@500&display=swap" rel="stylesheet">
<style>
  :root {
    --backdrop: #1b2328;
    --ink: #231f20;
    --paper: #ffffff;
    --wood-light: #efdcb8;
    --wood-mid: #e8d0a4;
    --wood-dark: #dfc393;
    --figure: #232121;
  }
  * { margin: 0; padding: 0; box-sizing: border-box; }
  html, body {
    width: 1200px;
    height: 1102px;
    overflow: hidden;
    background: var(--backdrop);
  }
  .canvas {
    position: relative;
    width: 1200px;
    height: 1102px;
  }
  .label {
    position: absolute;
    left: 317px;
    width: 567px;
    height: 472px;
    color: var(--ink);
  }
  .label--white { top: 66px; background: var(--paper); }
  .label--wood {
    top: 564px;
    background:
      radial-gradient(ellipse 70% 30% at 60% 20%, rgba(255,255,255,0.18), transparent 70%),
      radial-gradient(ellipse 80% 25% at 30% 75%, rgba(200,160,100,0.15), transparent 70%),
      linear-gradient(160deg, var(--wood-light) 0%, var(--wood-mid) 55%, var(--wood-dark) 100%);
  }
  .label__figure {
    position: absolute;
    left: 46px;
    top: 54px;
    width: 198px;
    height: 396px;
    background: var(--figure);
    border-radius: 46% 46% 48% 48% / 22% 22% 40% 40%;
  }
  .label__brand {
    position: absolute;
    left: 302px;
    top: 128px;
    font-family: "Bebas Neue", sans-serif;
    font-size: 35px;
    line-height: 1;
    letter-spacing: 0.2px;
    white-space: nowrap;
  }
  .label__title {
    position: absolute;
    left: 300px;
    top: 196px;
    font-family: "Bebas Neue", sans-serif;
    font-size: 76px;
    line-height: 56px;
    letter-spacing: -0.5px;
  }
  .label__title span { display: block; }
  .label__range {
    position: absolute;
    left: 306px;
    top: 382px;
    width: 192px;
    height: 32px;
    border-top: 3px solid var(--ink);
    border-bottom: 3px solid var(--ink);
    display: flex;
    align-items: center;
    padding: 0 10px 0 6px;
    font-family: "Oswald", sans-serif;
    font-weight: 500;
    font-size: 12px;
    letter-spacing: 1.6px;
  }
  .label__range-item:nth-child(2) { margin-left: 30px; }
  .label__range-item:nth-child(3) { margin-left: 14px; }
</style>
</head>
<body>
<main class="canvas">
  <section class="label label--white">
    <div class="label__figure" role="img" aria-label="Black silhouette illustration of a bearded man with swept hair, glasses and a curled moustache"></div>
    <p class="label__brand">Thornvale Goods Co</p>
    <h1 class="label__title"><span>Rugged</span><span>Ritual</span><span>Chest</span></h1>
    <p class="label__range"><span class="label__range-item">OILS</span><span class="label__range-item">BALMS</span><span class="label__range-item">SHAMPOO</span></p>
  </section>

  <section class="label label--wood">
    <div class="label__figure" role="img" aria-label="Black silhouette illustration of a bearded man with swept hair, glasses and a curled moustache"></div>
    <p class="label__brand">Thornvale Goods Co</p>
    <h2 class="label__title"><span>Rugged</span><span>Ritual</span><span>Chest</span></h2>
    <p class="label__range"><span class="label__range-item">OILS</span><span class="label__range-item">BALMS</span><span class="label__range-item">SHAMPOO</span></p>
  </section>
</main>
</body>
</html>
```